New modern website for Kerbline Groundworks

Hi we are an existing company that has a current website http://www.kerblinegroundworks.co.nz/ we are looking to get a new vibrant looking website designed to take us further and gain more customers. We are after a simple easy to use website that does not confuse but we want to make an impact and stand out from the rest

Target Market(s)

Homeowners And Commercial Businesses

Industry/Entity Type

It Company

Coding

Coded - Design and coding required

Number of Pages Required

2 page

```html
<!DOCTYPE html>
<html lang="en">
<head>
<meta charset="utf-8">
<title>Kerbline Groundworks</title>
<link href="https://fonts.googleapis.com/css2?family=Open+Sans:wght@300;400;600;700;800&family=Roboto+Condensed:wght@400;700&display=swap" rel="stylesheet">
<style>
:root{
  --ink:#16181c;
  --nav:#111316;
  --hero-a:#2b2e33;
  --hero-b:#16181b;
  --paper:#f2efea;
  --orange:#f06a1d;
  --yellow:#f3b61f;
  --red:#d0121b;
  --card:#2c2c2e;
  --navy:#2b2e44;
  --text:#333;
  --muted:#8a8c92;
  --white:#fff;
}
*{box-sizing:border-box;margin:0;padding:0}
html,body{width:1200px;height:3169px;overflow:hidden}
body{font-family:"Open Sans",sans-serif;background:var(--paper);color:var(--text);position:relative}
.abs{position:absolute}

/* nav */
.site-nav{position:absolute;left:0;top:0;width:1200px;height:63px;background:var(--nav);z-index:5}
.brand{left:162px;top:14px;color:var(--white);font:700 19px/1 "Roboto Condensed",sans-serif;letter-spacing:1px;text-transform:uppercase;display:flex;align-items:center;gap:8px;white-space:nowrap}
.brand-dot{width:12px;height:12px;background:var(--white);border-radius:50%}
.menu{left:458px;top:24px;display:flex;gap:18px;font-size:13px;color:#9ea1a7;white-space:nowrap}
.menu .active{color:var(--red)}
.nav-phone{left:828px;top:19px;color:var(--white);font:700 19px/1 "Open Sans",sans-serif;display:flex;gap:8px;align-items:center;white-space:nowrap}
.search{left:1013px;top:22px}

/* hero */
.hero{position:absolute;left:0;top:63px;width:1200px;height:497px;background:linear-gradient(160deg,var(--hero-a),var(--hero-b))}
.hero-photo{position:absolute;inset:0;background:radial-gradient(ellipse at 75% 35%,#4a4d52 0%,rgba(40,42,46,0) 55%),linear-gradient(180deg,rgba(0,0,0,0) 60%,rgba(0,0,0,.35))}
.hero-kicker{left:162px;top:95px;width:430px;text-align:center;color:var(--yellow);font-weight:700;font-size:15px}
.hero-kicker:before,.hero-kicker:after{content:"";position:absolute;top:10px;height:1px;width:100px;background:#777}
.hero-kicker:before{left:0}.hero-kicker:after{right:0}
.hero-title{left:156px;top:108px;color:var(--white);font:800 98px/1 "Open Sans",sans-serif;letter-spacing:-1px}
.hero-sub{left:252px;top:205px;color:#cfd1d4;font-size:26px;font-weight:300;white-space:nowrap}
.hero-text{left:162px;top:248px;width:430px;text-align:center;color:#c3c5c9;font-size:16px;line-height:22px}
.btn-outline{border:1px solid #8a8d92;color:var(--white);font-size:11px;font-weight:700;text-transform:uppercase;text-align:center}
.hero-btn{left:298px;top:319px;width:152px;height:36px;line-height:34px;background:rgba(0,0,0,.25)}
.arrow{top:222px;width:30px;height:62px;display:flex;align-items:center;justify-content:center}
.arrow-left{left:0;background:#111}
.arrow-right{right:0;background:var(--red)}

/* intro */
.peak-line{left:602px;top:560px;width:1px;height:14px;background:#333}
.years{left:0;top:580px;width:1200px;text-align:center;font-size:17px;color:#444}
.intro-title{left:0;top:622px;width:1200px;text-align:center;font-size:46px;font-weight:300;color:#222}
.intro-sub{left:0;top:680px;width:1200px;text-align:center;font:700 35px/1 "Open Sans",sans-serif;color:var(--orange);text-transform:uppercase;letter-spacing:-.5px}
.feature{top:765px;width:284px;height:350px;color:var(--white);text-align:center;overflow:hidden}
.feature-bg{position:absolute;inset:0}
.feature-icon{position:absolute;left:97px;top:50px;width:90px;height:90px;border-radius:50%;border:4px solid var(--white);background:rgba(0,0,0,.35)}
.feature h3{position:absolute;left:0;width:100%;top:165px;font-size:19px;font-weight:700;text-transform:uppercase;line-height:22px}
.feature p{position:absolute;left:22px;right:22px;top:205px;font-size:12.5px;line-height:18px;color:#c9cacc}

/* services */
.services{position:absolute;left:0;top:1210px;width:1200px;height:575px;background:linear-gradient(120deg,#2a2c30,#1d1f22)}
.services-photo{position:absolute;inset:0;background:linear-gradient(90deg,rgba(90,80,40,.25),rgba(0,0,0,0) 15%),radial-gradient(ellipse at 60% 50%,rgba(70,72,76,.6),rgba(0,0,0,0) 60%)}
.circle{border-radius:50%;border:14px solid rgba(70,72,78,.9)}
.circle-lg{left:169px;top:100px;width:262px;height:262px;background:linear-gradient(180deg,#b9c3c8,#8a9195)}
.circle-sm{left:376px;top:285px;width:170px;height:170px;background:linear-gradient(180deg,#9fb1c0,#7a7060)}
.services h2{position:absolute;left:634px;top:112px;color:var(--white);font-size:58px;font-weight:800}
.services h4{position:absolute;left:634px;top:196px;color:var(--white);font-size:24px;font-weight:700;line-height:32px;width:440px}
.services p{position:absolute;left:634px;top:271px;width:430px;color:#c3c5c9;font-size:13.5px;line-height:20px}
.btn-red{left:634px;top:415px;width:154px;height:38px;line-height:38px;background:var(--red);color:var(--white);font-size:11px;font-weight:700;text-align:center;text-transform:uppercase}

/* projects */
.projects-title{left:0;top:1858px;width:1200px;text-align:center;font-size:48px;font-weight:800;color:var(--orange)}
.projects-text{left:300px;top:1922px;width:600px;text-align:center;font-size:15px;line-height:21px;color:#333}
.tile{position:absolute}
.view-all{left:526px;top:2381px;width:150px;height:38px;line-height:36px;color:#222;border-color:#ccc;background:var(--paper)}

/* call to action */
.cta{position:absolute;left:0;top:2504px;width:1200px;height:274px;background:linear-gradient(180deg,#2a2c30,#1b1d20)}
.cta p{position:absolute;left:0;top:68px;width:1200px;text-align:center;color:#e8e8e8;font-size:32px;font-weight:300;line-height:42px}

/* footer */
.footer{position:absolute;left:0;top:2778px;width:1200px;height:391px;background:var(--navy);color:var(--white);border-top:3px solid var(--white)}
.footer h5{position:absolute;top:98px;color:var(--yellow);font-size:18px;font-weight:600;white-space:nowrap}
.links{position:absolute;top:138px;list-style:none;font-size:11.5px;color:#d8d9df}
.links li{height:24px;display:flex;align-items:center;gap:10px;white-space:nowrap}
.links li:before{content:"";width:6px;height:6px;border-radius:50%;background:#6c7086}
.links li.current:before{background:#5a8be0}
.field{position:absolute;left:539px;width:211px;height:26px;background:var(--white);color:#555;font-size:11px;line-height:26px;padding-left:8px}
.subscribe{position:absolute;left:539px;top:205px;width:211px;height:26px;background:var(--yellow);color:var(--white);font-size:14px;text-align:center;line-height:26px;text-transform:uppercase}
.ask{position:absolute;left:803px;top:84px;width:250px;font-size:18px;font-weight:700;line-height:24px}
.phones{position:absolute;left:803px;top:160px;display:flex;gap:16px;align-items:center;font-size:18px;font-weight:600;line-height:28px;white-space:nowrap}
.follow{position:absolute;left:803px;top:236px;display:flex;align-items:center;gap:8px;font-size:11px;white-space:nowrap}
.social{width:24px;height:24px;border-radius:50%;border:1.5px solid var(--white)}
.rule{position:absolute;left:160px;top:300px;width:880px;height:1px;background:#3e4259}
.copyright{position:absolute;left:0;top:321px;width:1200px;text-align:center;font-size:12px;color:#d0d2da}
</style>
</head>
<body>

<header class="site-nav">
  <div class="abs brand"><span class="brand-dot"></span>Kerbline Groundworks</div>
  <nav class="abs menu"><span class="active">Home</span><span>About</span><span>Services</span><span>Projects</span><span>Contact Us</span></nav>
  <div class="abs nav-phone">
    <svg width="18" height="18" viewBox="0 0 24 24"><path fill="#fff" d="M6.6 10.8a15 15 0 006.6 6.6l2.2-2.2c.3-.3.7-.4 1-.2 1.1.4 2.3.6 3.6.6.6 0 1 .4 1 1V20c0 .6-.4 1-1 1A17 17 0 013 4c0-.6.4-1 1-1h3.5c.6 0 1 .4 1 1 0 1.3.2 2.5.6 3.6.1.3 0 .7-.2 1z"/></svg>
    09-555-0142
  </div>
  <svg class="abs search" width="20" height="20" viewBox="0 0 20 20"><circle cx="8" cy="8" r="6" fill="none" stroke="#555" stroke-width="2.2"/><line x1="12.5" y1="12.5" x2="18" y2="18" stroke="#555" stroke-width="2.4"/></svg>
</header>

<section class="hero">
  <div class="hero-photo" role="img" aria-label="Trucks on a freshly paved road at dusk"></div>
  <div class="abs hero-kicker">Setting the standards for</div>
  <h1 class="abs hero-title">QUALITY</h1>
  <div class="abs hero-sub">Concrete &amp; Asphalters</div>
  <p class="abs hero-text">This is Layoutsmith's version of Lorem Ipsum. Proin gravida nibh vel velit auctor aliquet.</p>
  <div class="abs btn-outline hero-btn">Learn More</div>
  <div class="abs arrow arrow-left"><svg width="12" height="16" viewBox="0 0 12 16"><path d="M9 2L3 8l6 6" stroke="#fff" stroke-width="2.5" fill="none"/></svg></div>
  <div class="abs arrow arrow-right"><svg width="12" height="16" viewBox="0 0 12 16"><path d="M3 2l6 6-6 6" stroke="#fff" stroke-width="2.5" fill="none"/></svg></div>
</section>

<div class="abs peak-line"></div>
<div class="abs years">Years of experience</div>
<h2 class="abs intro-title">The trusted name for all Concrete &amp;</h2>
<div class="abs intro-sub">Asphalt Paving in Auckland</div>

<article class="abs feature" style="left:169px">
  <div class="feature-bg" role="img" aria-label="Crew laying asphalt at dusk" style="background:linear-gradient(180deg,#3a3b3d,#232325)"></div>
  <div class="feature-icon"></div>
  <h3>Our Expertise</h3>
  <p>We have a reputation with clients in and around Auckland for achieving great results on time and within budget every time. We are proud to share our years of experience.</p>
</article>
<article class="abs feature" style="left:458px">
  <div class="feature-bg" role="img" aria-label="Worker in hi-vis gear on a paving site" style="background:linear-gradient(180deg,#4a3a2c,#262424)"></div>
  <div class="feature-icon">
    <svg width="82" height="82" viewBox="0 0 82 82"><path d="M22 42 L41 25 L60 42 M28 38 V57 H54 V38" fill="none" stroke="#fff" stroke-width="4"/><rect x="37" y="45" width="8" height="12" fill="#fff"/></svg>
  </div>
  <h3>Concreting<br>&amp; Asphalt Work</h3>
  <p style="top:226px">When it comes to all asphalt services, you can rest assured we will work around your schedule, requirements and budget. Servicing throughout Auckland, we specialise in.</p>
</article>
<article class="abs feature" style="left:748px">
  <div class="feature-bg" role="img" aria-label="Asphalt being raked on a road" style="background:linear-gradient(180deg,#444240,#2a2928)"></div>
  <div class="feature-icon"></div>
  <h3>Additional Services</h3>
  <p>As part of our asphalt services, we are proud to offer a range of related services to our clients in the eastern suburbs and greater Auckland. Specialising in residential, commercial and</p>
</article>

<section class="services">
  <div class="services-photo" role="img" aria-label="Dark asphalt road surface with yellow markings"></div>
  <div class="abs circle circle-lg" role="img" aria-label="Crew finishing a concrete slab"></div>
  <div class="abs circle circle-sm" role="img" aria-label="Paving machinery on a job site"></div>
  <h2>SERVICES</h2>
  <h4>Complete asphalt services for your next project in Auckland</h4>
  <p>As your local one-stop shop you will receive durable solutions by calling on Kerbline Groundworks for all asphalt services. Arriving at your property in Auckland at an agreed upon time, we promise to leave no mess behind, only quality results. So please feel free to call us today to discuss what we can do for your project.</p>
  <div class="abs btn-red">Read More</div>
</section>

<h2 class="abs projects-title">PROJECTS</h2>
<p class="abs projects-text">This is Layoutsmith's version of Lorem Ipsum. Proin gravida nibh vel velit auctor aliquet. Aenean sollicitudin.</p>
<div class="tile" role="img" aria-label="Red chip garden driveway" style="left:163px;top:1997px;width:279px;height:342px;background:linear-gradient(180deg,#5d7a4a 0%,#7a6450 35%,#9a5d42 100%)"></div>
<div class="tile" role="img" aria-label="New asphalt with traffic cones" style="left:446px;top:1997px;width:353px;height:168px;background:linear-gradient(180deg,#8a8676,#3c3c3e)"></div>
<div class="tile" role="img" aria-label="Red truck carrying a roller" style="left:446px;top:2169px;width:353px;height:170px;background:linear-gradient(180deg,#b8c2c8,#a13a36 60%,#555)"></div>
<div class="tile" role="img" aria-label="Paved driveway beside a timber retaining wall" style="left:803px;top:1997px;width:234px;height:342px;background:linear-gradient(180deg,#8fa77a,#c8a15e 45%,#3a3a3c)"></div>
<div class="abs btn-outline view-all">View All</div>

<section class="cta" role="img" aria-label="Residential driveway at night">
  <p>For residential driveways and commercial<br>paving in Auckland</p>
</section>

<footer class="footer">
  <h5 style="left:160px">Quick Links</h5>
  <ul class="links" style="left:160px"><li class="current">Home</li><li>About</li><li>Services</li><li>Projects</li><li>Contact Us</li></ul>
  <h5 style="left:336px">Services</h5>
  <ul class="links" style="left:336px"><li>Lorem Ipsum dummy text</li><li>Lorem Ipsum dummy text</li><li>Lorem Ipsum dummy text</li><li>Lorem Ipsum dummy text</li><li>Lorem Ipsum dummy text</li></ul>
  <h5 style="left:539px">Signup Our Newsletters</h5>
  <div class="field" style="top:142px">Your Name</div>
  <div class="field" style="top:175px">Email Address</div>
  <div class="subscribe">Submit</div>
  <div class="ask">Any Questions you would like to ask? Need to talk to us</div>
  <div class="phones">
    <svg width="22" height="36" viewBox="0 0 22 36"><path fill="#fff" d="M5 10a14 14 0 006 10l2-2c.3-.3.7-.3 1 0l3 2c.3.3.3.7 0 1l-2 3C8 22 2 15 2 8l3-2c.3-.3.7-.2 1 0l2 3c.2.3.2.7 0 1z"/></svg>
    <div>09 55 50 142<br>027 555 0198</div>
  </div>
  <div class="follow">Follow Us On: <span class="social" style="margin-left:10px"></span><span class="social"></span><span class="social"></span><span class="social"></span></div>
  <div class="rule"></div>
  <div class="copyright">©2016 Copyright Kerblinegroundworks . All Rights Reserved. Privacy Policy - Terms of Service</div>
</footer>

</body>
</html>
```